Crestline Decor Depot needs Business cards and letterhead

letterhead, envelope & business card
Letterhead:
Crestline Decor Depot
4823 Larkfield Drive Bozeman, MT 59744
Phone #: (406) 555-0148
Fax#: (406) 555-0192
Business cards:
Crestline Decor Depot
Phone #: (406) 555-0148
Fax#: (406) 555-0192
Corinne Vasko
corinne@crestlinedecordepot.example
www.crestlinedecordepot.example
Target Market(s)
Home Interiors client
Industry/Entity Type
Business
Requirements
Must have
- ONLY submit straight front view on white background
- I DO NOT WANT ANY MOCK UPS
Nice to have
- see attached logo use guide
Should not have

```html
<!DOCTYPE html>
<html lang="en">
<head>
<meta charset="utf-8">
<title>Crestline Decor Depot — Business Card</title>
<link rel="stylesheet" href="https://fonts.googleapis.com/css2?family=Lato:wght@400;700&display=swap">
<style>
  :root {
    --brand-blue: #1273bf;
    --text-grey: #555a5f;
    --logo-grey: #5f6366;
    --card-white: #ffffff;
    --backdrop: #eceef0;
  }
  * { box-sizing: border-box; margin: 0; padding: 0; }
  html, body {
    width: 1200px; height: 1000px; overflow: hidden;
    background: var(--backdrop);
    font-family: "Lato", sans-serif;
  }
  .canvas { position: relative; width: 1200px; height: 1000px; }
  .card {
    position: absolute; left: 347px; width: 518px; height: 305px;
    background: var(--card-white);
    border: 1px solid #dcdfe2;
  }
  .card--front { top: 148px; }
  .card--back { top: 528px; }

  .brand {
    position: absolute; display: flex; align-items: center; gap: 8px;
    color: var(--logo-grey); font-weight: 700; text-transform: uppercase;
    white-space: nowrap;
  }
  .brand__square { background: var(--brand-blue); flex: none; }
  .card--front .brand { left: 42px; top: 80px; font-size: 15px; letter-spacing: 0.3px; }
  .card--front .brand__square { width: 12px; height: 12px; }
  .card--back .brand { left: 50%; top: 160px; transform: translateX(-50%); font-size: 22px; letter-spacing: 0.5px; }
  .card--back .brand__square { width: 16px; height: 16px; }

  .holder { position: absolute; right: 38px; top: 70px; text-align: right; }
  .holder__name { color: var(--brand-blue); font-weight: 700; font-size: 19px; letter-spacing: 0.2px; text-transform: uppercase; }
  .holder__title { color: var(--text-grey); font-size: 12px; margin-top: 2px; }

  .address { position: absolute; left: 40px; top: 180px; color: var(--text-grey); font-size: 12px; line-height: 17px; }
  .contacts { position: absolute; left: 40px; top: 222px; list-style: none; color: var(--text-grey); font-size: 12px; }
  .contacts li { display: flex; align-items: center; gap: 6px; height: 17.5px; }
  .contacts svg { width: 11px; height: 11px; fill: var(--brand-blue); flex: none; }

  .web-rule { position: absolute; left: 0; right: 0; display: flex; align-items: center; }
  .card--front .web-rule { top: 276px; }
  .card--back .web-rule { top: 271px; }
  .web-rule__line { height: 4px; background: var(--brand-blue); }
  .web-rule__line--long { flex: 1; }
  .web-rule__line--short { width: 29px; }
  .web-rule__url { color: var(--text-grey); font-size: 12px; padding: 0 7px; }
</style>
</head>
<body>
<main class="canvas">
  <section class="card card--front" aria-label="Business card front">
    <div class="brand"><span class="brand__square"></span>Crestline Decor Depot</div>
    <div class="holder">
      <p class="holder__name">Corinne Vasko</p>
      <p class="holder__title">General Manager</p>
    </div>
    <address class="address">4823 Larkfield Drive Bozeman<br>MT 59744</address>
    <ul class="contacts">
      <li><svg viewBox="0 0 24 24" aria-hidden="true"><path d="M6.6 10.8a15.1 15.1 0 0 0 6.6 6.6l2.2-2.2a1 1 0 0 1 1-.25 11.4 11.4 0 0 0 3.6.57 1 1 0 0 1 1 1V20a1 1 0 0 1-1 1A17 17 0 0 1 3 4a1 1 0 0 1 1-1h3.5a1 1 0 0 1 1 1c0 1.25.2 2.45.57 3.57a1 1 0 0 1-.25 1z"/></svg>(406) 555-0148</li>
      <li><svg viewBox="0 0 24 24" aria-hidden="true"><path d="M6 2h12v5H6zM3 8h18a1 1 0 0 1 1 1v8h-4v5H6v-5H2V9a1 1 0 0 1 1-1zm5 7v5h8v-5z"/></svg>(406) 555-0192</li>
      <li><svg viewBox="0 0 24 24" aria-hidden="true"><path d="M2 5h20v2l-10 6L2 7zm0 4.3l10 6 10-6V19H2z"/></svg>corinne@crestlinedecordepot.example</li>
    </ul>
    <div class="web-rule">
      <span class="web-rule__line web-rule__line--long"></span>
      <span class="web-rule__url">www.crestlinedecordepot.example</span>
      <span class="web-rule__line web-rule__line--short"></span>
    </div>
  </section>

  <section class="card card--back" aria-label="Business card back">
    <div class="brand"><span class="brand__square"></span>Crestline Decor Depot</div>
    <div class="web-rule">
      <span class="web-rule__line web-rule__line--long"></span>
      <span class="web-rule__url">www.crestlinedecordepot.example</span>
      <span class="web-rule__line web-rule__line--short"></span>
    </div>
  </section>
</main>
</body>
</html>
```